Website design to promote trampoline business

We require a website design for our business. The business is primarily provising access for people between 5YO and 40YO to jump on trampolines for fun and fitness.

We have a logo and color schemes already and the website should incorporate these colors and designs.

We would like to incorporate the following pages:-

Book Now!
Home
About Us
Locations & Hours
Jumping
Groups & Events
Gallery
Safety
Latest News
Careers

Industry/Entity Type

Business

Requirements
Must have
• Incorporate our logo and colors (files attached).

```html
<!DOCTYPE html>
<html lang="en">
<head>
<meta charset="utf-8">
<title>Skyleap Trampolines</title>
<link href="https://fonts.googleapis.com/css2?family=Open+Sans:wght@400;600;700&display=swap" rel="stylesheet">
<style>
:root{
  --orange:#f0a21b;
  --orange-dark:#d8870c;
  --blue:#41a6de;
  --ink:#444;
  --muted:#8a8a8a;
  --light:#f2f2f2;
  --rule:#e2e2e2;
  --dark:#2b2b2b;
  --white:#fff;
}
*{margin:0;padding:0;box-sizing:border-box}
html,body{width:828px;height:1200px;overflow:hidden;background:var(--white)}
body{font-family:"Open Sans",Arial,sans-serif;color:var(--ink);position:relative}
.site-header{height:56px;display:flex;align-items:center;justify-content:space-between;padding:0 90px}
.brand{display:flex;align-items:center;gap:8px;font-weight:700;font-size:20px;color:var(--dark);letter-spacing:.5px}
.brand-mark{width:18px;height:18px;background:var(--orange)}
.search{width:150px;height:22px;background:var(--dark);border-radius:2px;color:#aaa;font-size:9px;padding:5px 8px}
.main-nav{height:22px;background:var(--orange);display:flex;align-items:center;padding:0 90px;gap:20px}
.main-nav a{color:var(--white);font-size:8.5px;font-weight:600;text-decoration:none;text-transform:uppercase}
.hero{height:330px;position:relative;background:linear-gradient(90deg,#cfd4d2 0%,#e9ecea 45%,#f3f4f3 100%)}
.hero-photo{position:absolute;left:90px;top:0;width:360px;height:330px;background:radial-gradient(ellipse at 50% 60%,#9aa389 0%,#c7cbbf 45%,rgba(230,233,230,0) 75%)}
.hero-copy{position:absolute;right:90px;top:118px;width:300px;text-align:right}
.hero-copy h2{font-size:22px;font-weight:600;color:var(--dark);margin-bottom:10px}
.hero-copy p{font-size:11px;color:#666;line-height:1.45}
.btn{display:inline-block;margin-top:22px;background:var(--orange);color:var(--white);font-size:10px;font-weight:600;padding:8px 16px;border-radius:2px}
.hero-arrows{position:absolute;right:90px;bottom:14px;display:flex;gap:6px}
.hero-arrows span{width:16px;height:16px;border-radius:50%;background:#666;display:block}
.welcome{height:240px;text-align:center;padding:40px 90px 0}
.section-title{font-size:24px;font-weight:400;color:#555;margin-bottom:10px}
.rule{width:650px;height:1px;background:var(--rule);margin:0 auto 16px}
.welcome p{font-size:9px;color:var(--muted);line-height:1.7;max-width:650px;margin:0 auto}
.features{height:300px;background:var(--blue);display:grid;grid-template-columns:1fr 1fr;column-gap:30px;row-gap:30px;padding:38px 90px;color:var(--white)}
.feature h3{display:flex;align-items:center;gap:10px;font-size:17px;font-weight:600;text-transform:uppercase;margin-bottom:8px}
.feature svg{width:26px;height:24px}
.feature p{font-size:9.5px;line-height:1.6;opacity:.95}
.testimonial{height:150px;background:var(--light);text-align:center;padding:26px 90px 0}
.testimonial h2{font-size:20px;font-weight:400;color:#555;margin-bottom:10px}
.quote{position:relative;max-width:600px;margin:0 auto;font-size:8.5px;color:var(--muted);line-height:1.7}
.quote::before,.quote::after{position:absolute;font-size:30px;color:#999;top:-10px}
.quote::before{content:"\201C";left:-28px}
.quote::after{content:"\201D";right:-28px}
.quote cite{display:block;font-style:normal;margin-top:8px;color:#777}
.contact{height:172px;text-align:center;padding:28px 90px 0}
.contact h2{font-size:20px;font-weight:400;color:#555;margin-bottom:8px}
.contact p{font-size:9px;color:var(--muted);line-height:1.6;max-width:620px;margin:0 auto}
.social{display:flex;justify-content:center;gap:66px;margin-top:28px}
.social span{width:26px;height:26px;border-radius:50%;background:#888;display:block}
.site-footer{position:absolute;left:0;bottom:0;width:828px;height:30px;background:var(--dark);color:#bbb;font-size:9px;display:flex;align-items:center;justify-content:center}
</style>
</head>
<body>
<header class="site-header">
  <div class="brand"><span class="brand-mark"></span>Skyleap</div>
  <div class="search">Search here</div>
</header>
<nav class="main-nav">
  <a>Home</a><a>About Us</a><a>Locations &amp; Hours</a><a>Jumping</a><a>Groups &amp; Events</a><a>Gallery</a><a>Safety</a><a>Latest News</a><a>Careers</a>
</nav>
<section class="hero">
  <div class="hero-photo" role="img" aria-label="Photo of cupped hands holding a small young tree"></div>
  <div class="hero-copy">
    <h2>PELLENTESQUE BLANDIT RUT</h2>
    <p>Fusce vitae lacinia. Donec libero lorem hendrerit sed condimentum eget leo. Ut nec dictum nisl. Sed eleifend laoreet lacus nec dignissim.</p>
    <span class="btn">Book Now &rsaquo;</span>
  </div>
  <div class="hero-arrows"><span></span><span></span></div>
</section>
<section class="welcome">
  <h2 class="section-title">Welcome!</h2>
  <div class="rule"></div>
  <p>Ut tincidunt eget elementum dui lorem morbi leo. Nam posuere dui nec ante posuere faucibus varius. Donec blandit nisi magna, sed dignissim rutrum tortor sagittis. Nulla facilisi. Quisque tempus orci sit amet purus posuere, at rhoncus mauris fermentum. Integer vel velit quis justo pulvinar molestie vitae non ipsum. Vestibulum ante ipsum primis in faucibus orci luctus et ultrices posuere cubilia.</p>
</section>
<section class="features">
  <div class="feature">
    <h3><svg viewBox="0 0 26 24"><rect x="2" y="14" width="5" height="8" fill="#fff"/><rect x="10" y="9" width="5" height="13" fill="#fff"/><rect x="18" y="4" width="5" height="18" fill="#fff"/></svg>Solutions</h3>
    <p>Lorem ipsum dolor sit amet, consectetur adipiscing elit. Donec non sem vel orci tincidunt vitae. Phasellus quam nulla, fringilla at vestibulum eu, cursus ac magna pretium.</p>
  </div>
  <div class="feature">
    <h3><svg viewBox="0 0 26 24"><path d="M12 3a9 9 0 1 0 9 9h-9z" fill="#fff"/><path d="M14 1v9h9a9 9 0 0 0-9-9z" fill="#fff"/></svg>Analysis</h3>
    <p>Lorem ipsum dolor sit amet, consectetur adipiscing elit. Donec non sem vel orci tincidunt vitae. Phasellus quam nulla, fringilla at vestibulum eu, cursus ac magna pretium.</p>
  </div>
  <div class="feature">
    <h3><svg viewBox="0 0 26 24"><circle cx="13" cy="12" r="9" fill="none" stroke="#fff" stroke-width="2"/><circle cx="13" cy="12" r="4" fill="#fff"/></svg>Strategies</h3>
    <p>Lorem ipsum dolor sit amet, consectetur adipiscing elit. Donec non sem vel orci tincidunt vitae. Phasellus quam nulla, fringilla at vestibulum eu, cursus ac magna pretium.</p>
  </div>
  <div class="feature">
    <h3><svg viewBox="0 0 26 24"><rect x="9" y="3" width="8" height="5" fill="none" stroke="#fff" stroke-width="2"/><rect x="2" y="7" width="22" height="15" rx="2" fill="#fff"/></svg>Experience</h3>
    <p>Lorem ipsum dolor sit amet, consectetur adipiscing elit. Donec non sem vel orci tincidunt vitae. Phasellus quam nulla, fringilla at vestibulum eu, cursus ac magna pretium.</p>
  </div>
</section>
<section class="testimonial">
  <h2>Customer Testimonial</h2>
  <div class="quote">Pellentesque blandit rutrum lacus vitae luctus. Donec libero lorem hendrerit condimentum eget leo. Ut nec dictum nisl dignissim. Vivamus imperdiet felis vestibulum posuere aliquet. Aenean lacus sem, blandit at faucibus quis, laoreet nec lectus.<cite>Jane Doe</cite></div>
</section>
<section class="contact">
  <h2>Get in Touch</h2>
  <div class="rule"></div>
  <p>Lorem ipsum dolor sit amet, consectetur adipiscing elit. Maecenas vitae mollis vehicula neque et in urna odio. Etiam sit amet arcu ante, lorem ipsum dolor sit amet finibus.</p>
  <div class="social"><span></span><span></span><span></span><span></span><span></span></div>
</section>
<footer class="site-footer">Skyleap Trampolines (C) 2014 | PRIVACY POLICY</footer>
</body>
</html>
```